BrightLoop (1 page) homepage re-design

Our homepage needs a face-lift! We need our homepage on our website re-designed with a fresh and current look and feel. We have all the details, colour codes and a rough wireframe ready, but need a talented designer to put some personality into our ideas.

What we do: BrightLoop is a digital marketing agency with offices in Australia (Sydney) and South Africa (Cape Town). We specialise in SEO, PPC (otherwise known as Zentro PayLine or SEM), content marketing and Zentro Tallyboard. We use these tools to help our clients realise their business dreams.

VISUAL

Style / theme of the design:
Clean, simplistic, fun, flow.

Websites we draw inspiration from:
This is the theme we want to use to build the website
http://demo.vormalayouts.example/vl/?theme=Pebbled
Inspiration:
https://www.ondrapromo.example/
https://www.nelvagrowth.example.au/
https://quimbel.example.au/
https://torvin.layout-works.example/forum/

What we like about the site:
Clean, simple design, good use of white space. The subtle changing background colours, strong contrast with text. Not too busy or distracting.

What we don’t want: Too many different colours.

Target Market(s)

Our target audience: Marketing Managers of small to medium size businesses in Australia.

Industry/Entity Type

Marketing

Number of Pages Required

1 page

Font styles to use
Sans Serif

Requirements
Must have
• Elements to be added on homepage in order and as seen in attachments:
• - Section 1: Video with team as image and a play button add the heading: We help smart marketing managers achieve their KPIs [line break] and reduce their digital marketing overwhelm.
• - Section 2: Solutions section with the 6 solutions displayed in a row.
• - Section 3: Register Free Webinar with video
• - Section 4: Please add 3 case studies (as seen in attached docs there is only 1 but please add 3 below each other)
• - Section 5: Clients. Please add all client logo’s (black and white)
• - Section 6: Our Blog (as seen attached)
• - Section 7: Conferences Attended (please add the title and a paragraph of lorem Ipsom below) and then please add all conference logo’s attached below.
• - Section 8: In The Media (please add all logo’s titled media) white background
• - Section 9: Footer (dark grey footer) add our Zentro honoured affiliate logo here please
• - Section10: Footer - include:
• - Social logos (WorkMesh, Blipster, Pallwall, ReelDrop, Zentro Hub)
• - Navigation
• - Contact details (name, address, phone number, email)
• Colour codes:
• We want to use light greys, white and charcoal grey for the backgrounds with a pop of our green colour to bring out our branding and all CTA’s to be orange, colour codes below:
• Light grey: #F2F2F2
• Charcoal grey: #161616
• Green: #428E29
• CTA’s: #de7532
• PLEASE NOTE: Please see attached pdf titled: homepagecopybrief.pdf for all the titles and statistics that need to go on the homepage
Should not have
• Too much colour, icons should not be different colours

```html
<!DOCTYPE html>
<html lang="en">
<head>
<meta charset="utf-8">
<title>BrightLoop — Digital Marketing Agency</title>
<link href="https://fonts.googleapis.com/css2?family=Oswald:wght@400;500&family=Open+Sans:wght@400;600;700&display=swap" rel="stylesheet">
<style>
:root{
  --green:#428e29;
  --orange:#de7532;
  --orange-dark:#c9602a;
  --charcoal:#161616;
  --footer:#1f232a;
  --light:#f2f2f2;
  --lighter:#f8f8f8;
  --text:#555;
  --heading:#222;
  --white:#fff;
}
*{box-sizing:border-box;margin:0;padding:0}
html,body{width:1200px;height:4423px;overflow:hidden}
body{font-family:"Open Sans",Arial,sans-serif;color:var(--text);font-size:12px;line-height:1.6;background:var(--white)}
.wrap{width:800px;margin:0 auto;position:relative;height:100%}
section,header,footer{position:relative;width:1200px;overflow:hidden}
h2.section-title{font-family:Oswald,"Arial Narrow",sans-serif;font-weight:400;font-size:32px;line-height:48px;color:var(--heading);text-align:center;display:flex;align-items:center;justify-content:center;gap:22px}
h2.section-title::before,h2.section-title::after{content:"";width:95px;height:2px;background:var(--green)}
.btn{display:inline-flex;align-items:center;justify-content:center;gap:8px;font-family:"Open Sans",sans-serif;font-weight:600;font-size:12px;text-transform:uppercase;text-decoration:none}

/* top bar + nav */
.topbar{height:35px;background:var(--light);border-bottom:1px solid #e4e4e4;font-size:11px;color:#777}
.topbar .wrap{display:flex;align-items:center;justify-content:space-between}
.topbar .contact{display:flex;gap:10px;align-items:center}
.topbar .contact span{display:flex;align-items:center;gap:6px;padding-right:10px;border-right:1px solid #ddd}
.topbar .follow{display:flex;gap:8px;align-items:center}
.topbar .dot{width:10px;height:10px;border-radius:50%;background:#999}
.navbar{height:75px;background:var(--white)}
.logo{position:absolute;left:0;top:14px;display:flex;align-items:center;gap:6px}
.logo .mark{width:28px;height:28px;background:var(--green)}
.logo .name{font-family:Oswald,sans-serif;font-size:30px;font-weight:500;color:var(--green);letter-spacing:1px;line-height:1}
.nav{position:absolute;right:0;top:10px;display:flex;gap:26px;list-style:none;font-size:13px;color:#333}
.nav .active{color:var(--green);border-bottom:2px solid var(--green);padding-bottom:4px;font-weight:600}
.call{position:absolute;right:0;top:44px;font-size:12px;color:#444;font-weight:600;display:flex;gap:6px;align-items:center}

/* hero */
.hero{height:510px;background:radial-gradient(circle at 30% 40%,#e58a4b 0,var(--orange) 45%,var(--orange-dark) 100%)}
.hero .art{position:absolute;left:133px;top:30px;width:427px;height:425px;border-radius:30px;background:linear-gradient(135deg,rgba(255,255,255,.28),rgba(255,255,255,.08))}
.hero .copy{position:absolute;left:580px;top:130px;width:450px;color:var(--white)}
.hero h1{font-family:Oswald,sans-serif;font-weight:500;font-size:72px;line-height:1;letter-spacing:1px}
.hero .lead{font-weight:700;font-size:15px;margin-top:16px;white-space:nowrap}
.hero p{font-size:12px;line-height:1.55;margin-top:8px;opacity:.95;width:420px}
.hero .actions{display:flex;gap:12px;margin-top:28px;margin-left:74px}
.btn-white{background:var(--white);color:var(--orange);width:127px;height:36px}
.btn-dark{background:#3a3a3a;color:var(--white);width:130px;height:36px}
.hero .dots{position:absolute;left:582px;top:422px;display:flex;gap:6px}
.hero .dots i{width:8px;height:8px;border-radius:50%;background:rgba(255,255,255,.5)}
.hero .dots i:first-child{background:var(--white)}

/* solutions */
.solutions{height:450px;background:var(--lighter);padding-top:58px}
.sol-grid{display:grid;grid-template-columns:repeat(3,250px);column-gap:25px;row-gap:40px;margin-top:38px}
.sol h3{font-size:12px;font-weight:700;color:#222;text-transform:uppercase;margin-bottom:6px;white-space:nowrap}
.sol .row{display:flex;gap:12px}
.sol .icon{flex:0 0 62px;height:62px;border:1px solid #ddd;background:var(--white);display:flex;align-items:center;justify-content:center}
.sol p{font-size:11px;line-height:1.5}
.sol .more{display:block;margin-top:4px;font-size:10px;font-weight:700;color:var(--green)}

/* webinar */
.webinar{height:420px;background:linear-gradient(90deg,#cfcfcf,#ececec 50%)}
.webinar .art{position:absolute;left:110px;top:40px;width:440px;height:340px;border-radius:20px;background:linear-gradient(160deg,#dfdfdf,#c7cfe0 60%,#e4b4a0)}
.webinar .panel{position:absolute;left:600px;top:0;width:600px;height:420px;background:#4c4c4c;color:#ddd;padding:40px 0 0 30px}
.webinar h2{font-family:Oswald,sans-serif;font-weight:400;font-size:34px;line-height:1.3;color:var(--white)}
.webinar .rule{width:40px;height:2px;background:var(--white);margin:8px 0 14px}
.webinar h4{font-size:12px;font-weight:700;color:var(--white);text-transform:uppercase;width:350px;line-height:1.5}
.webinar p{width:360px;margin-top:14px;font-size:12px}
.btn-outline{border:2px solid var(--orange);color:var(--white);width:138px;height:46px;margin-top:24px;background:transparent}

/* media */
.media{height:310px;background:var(--white);padding-top:56px}
.media-row{display:flex;justify-content:space-between;width:830px;margin:44px auto 0}
.media-row li{list-style:none;width:124px;height:124px;border-radius:50%;background:var(--white);box-shadow:0 6px 12px rgba(0,0,0,.14);display:flex;align-items:center;justify-content:center;font-weight:700;font-size:14px;color:#333;text-align:center;line-height:1.2}

/* clients */
.clients{height:265px;background:var(--lighter)}
.clients h2,.case h2{font-family:Oswald,sans-serif;font-weight:400;font-size:32px;line-height:1.3;color:var(--heading)}
.clients .intro{position:absolute;left:0;top:60px;width:330px}
.clients .intro p{margin-top:16px;font-size:12px}
.client-logos{position:absolute;left:400px;top:60px;width:400px;display:flex;flex-wrap:wrap;gap:24px 36px}
.client-logos span{font-weight:700;font-size:16px;color:#333;display:flex;align-items:center;gap:8px;height:40px}
.client-logos i{width:22px;height:22px;background:#333;display:inline-block}

/* case study */
.case{height:397px;background:var(--white)}
.case .copy{position:absolute;left:0;top:52px;width:380px}
.case .underline{width:100px;height:2px;background:var(--green);margin:4px 0 18px}
.case h4{font-size:12px;font-weight:700;color:#222;text-transform:uppercase;line-height:1.5}
.case p{margin-top:12px}
.btn-charcoal{background:#2f2f2f;color:var(--white);width:108px;height:38px;margin-top:22px}
.case .art{position:absolute;left:420px;top:30px;width:398px;height:300px;border-radius:16px;background:linear-gradient(135deg,#eef1f6,#d7dde8 60%,#f3d9b8)}

/* blog */
.blog{height:518px;background:linear-gradient(180deg,#e9e9e9,#dedede);padding-top:70px}
.cards{display:flex;gap:38px;margin-top:40px;padding-left:6px}
.card{width:236px;height:310px;background:var(--white);box-shadow:0 6px 16px rgba(0,0,0,.15)}
.card .thumb{height:133px}
.card .body{padding:14px}
.card h5{font-size:12px;font-weight:700;color:#222;text-transform:uppercase}
.card .date{font-size:11px;color:#888;margin:2px 0 6px}
.card p{font-size:11px;line-height:1.5}
.card .more{display:block;margin-top:6px;font-size:11px;font-weight:700}

/* learning */
.learning{height:350px;background:var(--white);padding-top:58px}
.learning p.lead{width:800px;margin:32px auto 0;text-align:center;font-size:12px}
.learn-logos{width:800px;margin:18px auto 0;border-top:1px solid #ccc;border-bottom:1px solid #ccc;height:90px;display:flex;align-items:center;gap:60px;padding-left:12px}
.learn-logos span{font-weight:700;font-size:22px;color:#222;display:flex;align-items:center;gap:10px}
.learn-logos i{width:30px;height:30px;border-radius:50%;background:#222;display:inline-block}

/* about */
.about{height:592px;background:var(--light);padding-top:46px}
.about .card-wrap{width:800px;height:512px;margin:0 auto;background:var(--white);box-shadow:0 4px 14px rgba(0,0,0,.08);padding-top:54px}
.about p.lead{width:560px;margin:22px auto 0;text-align:center;font-size:12px}
.team{display:flex;justify-content:center;gap:21px;margin-top:34px}
.member{width:156px;height:222px;border:1px solid #e5e5e5;text-align:center;padding-top:14px}
.member .avatar{width:106px;height:106px;border-radius:50%;margin:0 auto;background:linear-gradient(160deg,#b9b3ad,#5f5a57)}
.member h6{font-size:12px;font-weight:600;color:#222;margin-top:10px}
.member .role{font-size:10px;color:#888}
.member .socials{display:flex;justify-content:center;gap:6px;margin-top:8px}
.member .socials i{width:20px;height:20px;border-radius:50%;border:1px solid #aaa;display:inline-block}

/* footer */
.footer{height:501px;background:var(--footer);color:#bbb}
.footer .col{position:absolute;top:66px}
.footer h4{font-size:14px;font-weight:700;color:var(--white);display:flex;align-items:center;gap:10px}
.footer h4::after{content:"";width:56px;height:2px;background:var(--green)}
.footer .about-col{left:0;width:300px}
.footer .about-col p{margin-top:20px;font-size:11px;line-height:1.6}
.footer .social{display:flex;gap:8px;margin-top:18px}
.footer .social i{width:26px;height:26px;background:#2f343c;border:1px solid #444;display:inline-block}
.footer .links{left:354px}
.footer .links ul{list-style:none;margin-top:16px;font-size:12px;line-height:1.8;color:#ccc}
.footer .touch{left:569px;width:231px}
.footer form{margin-top:16px;display:flex;flex-direction:column}
.footer .field{height:35px;border-bottom:1px solid #555;display:flex;align-items:center;gap:10px;font-size:11px;color:#ccc}
.footer .submit{margin-top:14px;width:100px;height:30px;background:var(--white);color:#222;font-size:10px;font-weight:700;display:flex;align-items:center;justify-content:center}
.footer .bar{position:absolute;left:0;top:404px;width:800px;height:50px;background:#2b2f36;display:flex;align-items:center;justify-content:space-around;font-size:11px;color:#ddd}
.footer .bar span{display:flex;align-items:center;gap:8px}
.footer .copy{position:absolute;left:0;top:468px;width:800px;text-align:center;font-size:11px;color:#ddd}
</style>
</head>
<body>

<header>
  <div class="topbar">
    <div class="wrap">
      <div class="contact">
        <span><svg width="11" height="9" viewBox="0 0 11 9"><rect x=".5" y=".5" width="10" height="8" fill="none" stroke="#888"/><path d="M.5 .5l5 4 5-4" fill="none" stroke="#888"/></svg>info@brightloop.example</span>
        <span style="border:0"><svg width="8" height="11" viewBox="0 0 8 11"><path d="M4 10.5C1 6.5 .5 5.5.5 4a3.5 3.5 0 017 0c0 1.5-.5 2.5-3.5 6.5z" fill="#888"/></svg>22-24 Kestrel Lane, Harbourside NSW</span>
      </div>
      <div class="follow">Follow Us <i class="dot"></i><i class="dot"></i><i class="dot"></i></div>
    </div>
  </div>
  <div class="navbar">
    <div class="wrap">
      <div class="logo"><span class="mark"></span><span class="name">BRIGHTLOOP</span></div>
      <ul class="nav">
        <li class="active">Home</li><li>About</li><li>PPc</li><li>Seo</li><li>Training</li><li>Client Success</li><li>Blog</li><li>Resources</li><li>Contact</li>
      </ul>
      <div class="call"><svg width="11" height="11" viewBox="0 0 11 11"><path d="M2 .5l2 2.5-1 1.5c.8 1.5 1.9 2.6 3.4 3.4L8 7l2.5 2-1 1.5C5 10 1 6 .5 1.5z" fill="#444"/></svg>Call Us : 1300 555 014</div>
    </div>
  </div>
</header>

<section class="hero">
  <div class="art" role="img" aria-label="Illustration of a laptop, tablet and phone with chat bubbles and marketing icons"></div>
  <div class="copy">
    <h1>BRIGHTLOOP</h1>
    <div class="lead">Lorem Ipsum is simply dummy text of the printing</div>
    <p>Lorem Ipsum is simply dummy text of the printing and typesetting industry. Lorem Ipsum has been the industry's standard dummy text ever since a galley of type...</p>
    <div class="actions">
      <a class="btn btn-white">Watch Video <svg width="8" height="9"><path d="M0 0l8 4.5L0 9z" fill="#de7532"/></svg></a>
      <a class="btn btn-dark">Contact Us <svg width="8" height="9"><path d="M0 0l8 4.5L0 9z" fill="#fff"/></svg></a>
    </div>
  </div>
  <div class="dots"><i></i><i></i><i></i></div>
</section>

<section class="solutions">
  <div class="wrap" style="height:auto">
    <h2 class="section-title">Solutions</h2>
    <div class="sol-grid">
      <div class="sol"><h3>Grow Revenue</h3><div class="row"><span class="icon"><svg width="34" height="28"><rect x="2" y="16" width="6" height="12" fill="#666"/><rect x="12" y="10" width="6" height="18" fill="#666"/><rect x="22" y="3" width="6" height="25" fill="#428e29"/></svg></span><p>Lorem Ipsum is simply dummytext of the printing and typesettingindustry dummy text here...</p></div><span class="more">LEARN MORE</span></div>
      <div class="sol"><h3>Convert Leads</h3><div class="row"><span class="icon"><svg width="30" height="30"><circle cx="15" cy="15" r="12" fill="none" stroke="#666" stroke-width="3"/><path d="M9 15l4 4 8-8" fill="none" stroke="#428e29" stroke-width="3"/></svg></span><p>Lorem Ipsum is simply dummytext of the printing and typesettingindustry dummy text here...</p></div><span class="more">LEARN MORE</span></div>
      <div class="sol"><h3>Increase Brand Awareness</h3><div class="row"><span class="icon"><svg width="32" height="28"><path d="M3 11h6l12-8v22L9 17H3z" fill="#666"/><path d="M25 9c3 3 3 7 0 10" fill="none" stroke="#428e29" stroke-width="3"/></svg></span><p>Lorem Ipsum is simply dummytext of the printing and typesettingindustry dummy text here...</p></div><span class="more">LEARN MORE</span></div>
      <div class="sol"><h3>Data / KPIs</h3><div class="row"><span class="icon"><svg width="30" height="30"><ellipse cx="15" cy="6" rx="11" ry="4" fill="#666"/><rect x="4" y="6" width="22" height="18" fill="#666"/><ellipse cx="15" cy="24" rx="11" ry="4" fill="#666"/><path d="M4 13c4 3 18 3 22 0M4 19c4 3 18 3 22 0" stroke="#428e29" stroke-width="2" fill="none"/></svg></span><p>Lorem Ipsum is simply dummytext of the printing and typesettingindustry dummy text here...</p></div><span class="more">LEARN MORE</span></div>
      <div class="sol"><h3>Increase Engagement</h3><div class="row"><span class="icon"><svg width="30" height="30"><path d="M4 15a11 11 0 0119-7" fill="none" stroke="#428e29" stroke-width="3"/><path d="M26 15a11 11 0 01-19 7" fill="none" stroke="#666" stroke-width="3"/><path d="M21 3l3 6-6 0z" fill="#428e29"/><path d="M9 27l-3-6 6 0z" fill="#666"/></svg></span><p>Lorem Ipsum is simply dummytext of the printing and typesettingindustry dummy text here...</p></div><span class="more">LEARN MORE</span></div>
      <div class="sol"><h3>Marketing Strategy/Budgeting</h3><div class="row"><span class="icon"><svg width="30" height="30"><rect x="3" y="5" width="24" height="20" fill="none" stroke="#666" stroke-width="3"/><path d="M7 20l6-6 4 3 6-7" fill="none" stroke="#428e29" stroke-width="3"/></svg></span><p>Lorem Ipsum is simply dummytext of the printing and typesettingindustry dummy text here...</p></div><span class="more">LEARN MORE</span></div>
    </div>
  </div>
</section>

<section class="webinar">
  <div class="art" role="img" aria-label="Illustration of an SEO search bar, magnifier, colourful bar chart and rising arrow"></div>
  <div class="panel">
    <h2>Webinar</h2>
    <div class="rule"></div>
    <h4>Lorem Ipsum is simply dummy text of the printing and type-setting industry.</h4>
    <p>Lorem Ipsum is simply dummy text of the printing and typesettingindustry. Lorem Ipsum has been the industry's standard dummy text ever since the 1500s, when an unknown printer took a galley of type and scrambled it to make a type specimen book.......</p>
    <a class="btn btn-outline">Contact Us</a>
  </div>
</section>

<section class="media">
  <h2 class="section-title">In the Media</h2>
  <ul class="media-row">
    <li>Dailyfold</li><li>Soloway</li><li>Trademint</li><li>The Harbour<br>Ledger</li><li>MINDPLATE</li><li>The Evening<br>Courier</li>
  </ul>
</section>

<section class="clients">
  <div class="wrap">
    <div class="intro">
      <h2>Our Clients</h2>
      <p>Lorem Ipsum is simply dummy text of the printing and type-setting industry. Lorem Ipsum has been the industry's standard dummy text ever since the 1500s, it to make.</p>
    </div>
    <div class="client-logos">
      <span><i></i>Norvale</span><span>Quillpoint Editing</span><span>Stackwell Storage</span>
      <span>homescout</span><span>Ridgetank</span>
    </div>
  </div>
</section>

<section class="case">
  <div class="wrap">
    <div class="copy">
      <h2>Case Study</h2>
      <div class="underline"></div>
      <h4>Lorem Ipsum is simply dummy text of the printing and type-setting industry.</h4>
      <p>Lorem Ipsum is simply dummy text of the printing and typesettingindustry. Lorem Ipsum has been the industry's standard dummy text ever since the 1500s, when an unknown printer took a galley of type and scrambled it to make a type specimen book ......</p>
      <a class="btn btn-charcoal">Read More</a>
    </div>
    <div class="art" role="img" aria-label="Illustration of a desktop screen and tablet showing a yellow bar chart"></div>
  </div>
</section>

<section class="blog">
  <h2 class="section-title">Our Blog</h2>
  <div class="wrap" style="height:auto">
    <div class="cards">
      <article class="card"><div class="thumb" style="background:var(--green)" role="img" aria-label="Illustration of a laptop showing analytics charts"></div><div class="body"><h5>Lorem Ipsum Is Simply Dumy Text</h5><div class="date">3 Feb 2018</div><p>Lorem Ipsum is simply dummy text of the printing and typesetting industry. Lorem Ipsum has been the industry's.</p><span class="more" style="color:var(--green)">READ MORE &gt;&gt;</span></div></article>
      <article class="card"><div class="thumb" style="background:var(--orange)" role="img" aria-label="Illustration of a screen with an SEO magnifier"></div><div class="body"><h5>Lorem Ipsum Is Simply Dumy Text</h5><div class="date">3 Feb 2018</div><p>Lorem Ipsum is simply dummy text of the printing and typesetting industry. Lorem Ipsum has been the industry's.</p><span class="more" style="color:var(--orange)">READ MORE &gt;&gt;</span></div></article>
      <article class="card"><div class="thumb" style="background:#f6d95a" role="img" aria-label="Illustration of a laptop with marketing graphics"></div><div class="body"><h5>Lorem Ipsum Is Simply Dumy Text</h5><div class="date">3 Feb 2018</div><p>Lorem Ipsum is simply dummy text of the printing and typesetting industry. Lorem Ipsum has been the industry's.</p><span class="more" style="color:var(--green)">READ MORE &gt;&gt;</span></div></article>
    </div>
  </div>
</section>

<section class="learning">
  <h2 class="section-title">Learning</h2>
  <p class="lead">Lorem Ipsum is simply dummy text of the printing and typesetting industry. Lorem Ipsum has been the industry's standard dummy text ever since the 1500s, when an unknown printer took a galley of type and scrambled it to make a type specimen book. It has survived not only five centuries, but also the leap intoelectronic typesetting, remaining essentially...</p>
  <div class="learn-logos"><span><i></i>WEBCONVO</span><span><i></i>SRCH EXPO</span><span>RankSummit</span></div>
</section>

<section class="about">
  <div class="card-wrap">
    <h2 class="section-title">About Us</h2>
    <p class="lead">Lorem Ipsum is simply dummy text of the printing and typesetting industry. Lorem Ipsum has been the industry's standard dummy text ever since the 1500s, when an unknown printer took a galley of type and scrambled it to make a type specimen book. It has survived not only five remaining essentially.</p>
    <div class="team">
      <div class="member"><div class="avatar" role="img" aria-label="Team member portrait"></div><h6>Maren Holt</h6><div class="role">Web Developer</div><div class="socials"><i></i><i></i><i></i><i></i></div></div>
      <div class="member"><div class="avatar" role="img" aria-label="Team member portrait"></div><h6>Tobin Ward</h6><div class="role">Seo Developer</div><div class="socials"><i></i><i></i><i></i><i></i></div></div>
      <div class="member"><div class="avatar" role="img" aria-label="Team member portrait"></div><h6>Maren Holt</h6><div class="role">Web Developer</div><div class="socials"><i></i><i></i><i></i><i></i></div></div>
    </div>
  </div>
</section>

<footer class="footer">
  <div class="wrap">
    <div class="col about-col">
      <h4>About Company</h4>
      <p>Lorem Ipsum is simply dummy text of the printing and typesetting industry. Lorem Ipsum has been the industry's standard dummy text ever since the 1500s, when an unknown printer book...</p>
      <div class="social"><i></i><i></i><i></i><i></i><i></i></div>
    </div>
    <div class="col links">
      <h4>Quick Links</h4>
      <ul><li>Home</li><li>About</li><li>PPc's</li><li>Seo</li><li>Training</li><li>Client Success</li><li>Blog</li><li>Resources</li><li>Contact</li></ul>
    </div>
    <div class="col touch">
      <h4>Get In Touch</h4>
      <form>
        <div class="field"><svg width="10" height="10"><circle cx="5" cy="3" r="2.5" fill="#ccc"/><path d="M0 10a5 4 0 0110 0z" fill="#ccc"/></svg>Name</div>
        <div class="field"><svg width="10" height="10"><path d="M2 0l2 2.5-1 1.5c.8 1.5 1.9 2.6 3.4 3.4L8 6.5l2 2-1 1.5C5 9.5.5 5 .5 1z" fill="#ccc"/></svg>Phone</div>
        <div class="field"><svg width="11" height="9"><rect x=".5" y=".5" width="10" height="8" fill="none" stroke="#ccc"/><path d="M.5 .5l5 4 5-4" fill="none" stroke="#ccc"/></svg>E-mail</div>
        <div class="field"><svg width="8" height="11"><path d="M4 10.5C1 6.5 .5 5.5.5 4a3.5 3.5 0 017 0c0 1.5-.5 2.5-3.5 6.5z" fill="#ccc"/></svg>Address</div>
        <div class="submit">SUBMIT</div>
      </form>
    </div>
    <div class="bar">
      <span><svg width="11" height="11"><path d="M2 .5l2 2.5-1 1.5c.8 1.5 1.9 2.6 3.4 3.4L8 7l2.5 2-1 1.5C5 10 1 6 .5 1.5z" fill="#428e29"/></svg>Call : 1300 555 014</span>
      <span><svg width="11" height="9"><rect x=".5" y=".5" width="10" height="8" fill="none" stroke="#428e29"/><path d="M.5 .5l5 4 5-4" fill="none" stroke="#428e29"/></svg>E-mail : info@brightloop.example</span>
      <span><svg width="8" height="11"><path d="M4 10.5C1 6.5 .5 5.5.5 4a3.5 3.5 0 017 0c0 1.5-.5 2.5-3.5 6.5z" fill="#428e29"/></svg>Location : 22-24 Kestrel Lane, Harbourside NSW</span>
    </div>
    <div class="copy">© Copyright 2018 brightloop.example. All Rights Reserved.</div>
  </div>
</footer>

</body>
</html>
```